Copper Vale Tattoo

Business card / Appointment card in one

Ive attached the new logo along with a simple format of what I would like written out on the back! Would like a clean/ modern style font to be used! I also attached the current card for a reference of style!

The colors of this would be either white and gold lettering or black with gold lettering.

Email - CopperValeNB@inkmail.example
Ph # 555-482-9073

The message at bottom of back - All cancellations or No Call No Shows within 48 hours of appointment time will result in a forfeit of deposit.

Small block avail (if card is black) to write in appointment date/time

Target Market(s)

Card for Tattoo shop

Contact Information for Business Card

in project description area!

Font styles to use
Sans Serif

Requirements
Must have
• Please refer to current business card photos that were attached as well!
Nice to have
• Looking for blacks, greys and gold for color scheme

```html
<!DOCTYPE html>
<html lang="en">
<head>
<meta charset="utf-8">
<title>Copper Vale Tattoo — Business &amp; Appointment Card</title>
<link rel="stylesheet" href="https://fonts.googleapis.com/css2?family=Cinzel:wght@400;500&display=swap">
<style>
  :root {
    --backdrop: #2a2a2b;
    --card-black: #050505;
    --gold: #c9b25a;
    --gold-faint: rgba(201, 178, 90, 0.10);
    --ink-white: #eeeeee;
    --write-block: #f4f4f4;
  }
  * { margin: 0; padding: 0; box-sizing: border-box; }
  html, body {
    width: 1200px;
    height: 912px;
    overflow: hidden;
    background: var(--backdrop);
  }
  .card-pair {
    position: relative;
    width: 1200px;
    height: 912px;
    display: flex;
    justify-content: center;
    align-items: center;
    gap: 80px;
  }
  .card {
    position: relative;
    width: 380px;
    height: 664px;
    background: var(--card-black);
    border-radius: 4px;
    font-family: "Cinzel", serif;
    text-align: center;
    overflow: hidden;
    box-shadow: 0 18px 40px rgba(0, 0, 0, 0.45);
  }
  .card-front {
    display: flex;
    align-items: center;
    justify-content: center;
  }
  .brand-name {
    color: var(--gold);
    font-weight: 400;
    font-size: 34px;
    letter-spacing: 0.12em;
    line-height: 1.3;
  }
  .brand-mark {
    display: inline-block;
    width: 14px;
    height: 14px;
    border-radius: 50%;
    background: var(--gold);
    margin-bottom: 22px;
  }
  .card-back { padding: 46px 30px 0; }
  .back-watermark {
    position: absolute;
    top: 230px;
    left: 0;
    right: 0;
    color: var(--gold-faint);
    font-size: 58px;
    font-weight: 400;
    letter-spacing: 0.08em;
    line-height: 1.15;
  }
  .back-title {
    position: relative;
    color: var(--gold);
    font-weight: 400;
    font-size: 36px;
    letter-spacing: 0.14em;
    line-height: 1.35;
  }
  .contact {
    position: relative;
    margin-top: 50px;
    color: var(--ink-white);
    font-size: 15px;
    letter-spacing: 0.12em;
    line-height: 1.75;
    font-style: normal;
  }
  .contact .email { font-size: 13px; letter-spacing: 0.08em; }
  .policy {
    position: relative;
    margin-top: 54px;
    color: var(--gold);
    font-size: 15px;
    letter-spacing: 0.16em;
    line-height: 1.55;
    padding: 0 14px;
  }
  .appointment-block {
    position: absolute;
    left: 36px;
    right: 36px;
    bottom: 34px;
    height: 108px;
    background: var(--write-block);
    border-radius: 14px;
  }
</style>
</head>
<body>
  <main class="card-pair">
    <section class="card card-front" aria-label="Card front">
      <div class="brand-lockup">
        <span class="brand-mark" aria-hidden="true"></span>
        <p class="brand-name">Copper Vale<br>Tattoo</p>
      </div>
    </section>

    <section class="card card-back" aria-label="Card back">
      <p class="back-watermark" aria-hidden="true">Copper<br>Vale<br>Tattoo</p>
      <h1 class="back-title">Copper Vale<br>Tattoo</h1>
      <address class="contact">
        <span class="email">CopperValeNB@inkmail.example</span><br>
        <span class="phone">555-482-9073</span>
      </address>
      <p class="policy">All cancellations or no call no shows within 48 hours of appointment time will result in a forfeit of deposit.</p>
      <div class="appointment-block" aria-label="Space to write appointment date and time"></div>
    </section>
  </main>
</body>
</html>
```